Wordpress Design for my Consulting Company

We want a WordPress site created for our new business. We have created a mock-up of the content we want on the site at https://marcusdellow.example-sites.com/website-5

We are not attached to any of the pictures and just put stock stuff from wix's editor, which we don't have rights to use outside of wix.

We are NOT looking to just port this site to WordPress, we are looking for some creative ways to display the content in a more professional artistic sense.

I have included several logo files and a text file with the colors and Fonts used in the logo. We are not looking to change the logo or the colors used in the logo.

The Schedule appointment links to a page that embeds a bookingnest.example.com calendar. https://bookingnest.example.com/marcus-dellow/brightvale

The final website domain will be enterprisebrightvale.example

Enterprise brightvale is a consulting company that works directly with the business owners and leaders of small businesses between 50-200 employees. We help companies make sure they have the right technology to meet their strategic goals. We are the anti-"Computer Guy" and we focus on business outcomes NOT cool technology gadgets.

The final design should communicate business growth and success.

Target Market(s)

Business Owners of companies with 50-200 employees

Coding

Coded - Design and coding required

Number of Pages Required

1 page

Font styles to use
Serif
Other font styles liked:
• Trajan Pro Bold, Open Sans

Requirements
Must have
• Should focus on consulting rather than technology.
• Should show the customer as the hero and we are just their guide.
• Must use the logo provided and the colors and fonts in the text file provided. Any other colors and fonts must be complementary.
• The design should scale for all devices computer, iPad, or phone
Should not have
• Should not focus on technology, we are the anti-"Computer Guy" and we focus on business outcomes NOT cool technology gadgets.

```html
<!DOCTYPE html>
<html lang="en">
<head>
<meta charset="utf-8">
<title>Enterprise Brightvale – Technology Advisors That Get Business</title>
<link href="https://fonts.googleapis.com/css2?family=Cinzel:wght@400;700&family=Open+Sans:wght@400;600;700&display=swap" rel="stylesheet">
<style>
:root{
  --orange:#c7784c;
  --orange-dark:#b5673d;
  --slate:#27343a;
  --slate-2:#2f3d44;
  --ink:#3b3b3b;
  --muted:#6e6e6e;
  --paper:#ffffff;
  --mist:#ececec;
  --line:#d9d9d9;
}
*{box-sizing:border-box;margin:0;padding:0}
html,body{width:1200px;height:4114px;overflow:hidden}
body{position:relative;background:var(--paper);font-family:"Open Sans",Arial,sans-serif;color:var(--ink)}
.serif{font-family:"Cinzel","Times New Roman",serif}
.abs{position:absolute}
.btn{position:absolute;display:flex;align-items:center;justify-content:center;background:var(--orange);color:#fff;font-size:12px;font-weight:600;border-radius:16px;height:30px;letter-spacing:.3px}

/* header */
.site-header{left:0;top:0;width:1200px;height:69px;background:#fff}
.brand{left:172px;top:12px;display:flex;align-items:center;gap:10px}
.brand-dot{width:40px;height:40px;border-radius:50%;background:var(--slate)}
.brand-name{font-family:"Cinzel",serif;font-size:17px;font-weight:700;color:var(--slate);line-height:1.1}
.brand-tag{font-size:8px;color:var(--muted);letter-spacing:.4px}
.nav{right:172px;top:26px;display:flex;gap:34px;font-size:11px;letter-spacing:.6px;color:var(--slate);font-weight:600}

/* hero */
.hero{left:0;top:69px;width:1200px;height:514px;background:linear-gradient(100deg,#4b4f4f 0%,#6e726e 40%,#9a9b93 70%,#7d8177 100%)}
.hero-title{left:172px;top:243px;font-family:"Cinzel",serif;color:#fff;font-size:34px;font-weight:700;line-height:1.15}
.hero-sub{left:172px;top:330px;width:320px;color:#f1f1f1;font-size:14px;line-height:1.45}
/* intro */
.intro-title{left:172px;top:660px;font-family:"Cinzel",serif;font-size:25px;color:var(--slate);line-height:1.35}
.intro-title span{color:var(--orange);font-size:30px;letter-spacing:1px}
.intro-text{left:172px;top:760px;width:400px;font-size:12px;line-height:1.7;color:var(--muted)}
.we-get{left:617px;top:617px;width:412px;height:378px;background:var(--orange);box-shadow:0 4px 12px rgba(0,0,0,.25)}
.we-get h3{position:absolute;top:22px;width:100%;text-align:center;font-family:"Cinzel",serif;color:#fff;font-size:30px;font-weight:400;letter-spacing:2px}
.we-get .rule{position:absolute;left:0;top:80px;width:412px;height:1px;background:rgba(255,255,255,.45)}
.we-get .divide{position:absolute;left:206px;top:100px;width:1px;height:260px;background:rgba(255,255,255,.45)}
.get-item{position:absolute;width:170px;text-align:center;color:#fff;font-size:12px;font-weight:700;letter-spacing:.5px;line-height:1.4}

/* tired */
.tired-left{left:0;top:1074px;width:600px;height:693px;background:var(--orange)}
.tired-right{left:600px;top:1074px;width:600px;height:693px;background:var(--slate)}
.tired-frame{left:172px;top:1195px;width:476px;height:490px;border:3px solid #fff}
.tired-title{left:230px;top:1400px;font-family:"Cinzel",serif;color:#fff;font-size:38px;line-height:1.2}
.timeline{left:700px;top:1105px;width:1px;height:630px;background:rgba(255,255,255,.35)}
.tl-item{position:absolute;left:692px;width:320px;color:#fff;font-size:12.5px;line-height:1.6}
.tl-item::before{content:"";position:absolute;left:0;top:4px;width:15px;height:15px;border-radius:50%;background:var(--orange)}
.tl-item p{margin-left:70px}

/* testimonial */
.proof-intro{left:172px;top:1822px;width:860px;font-size:12px;line-height:1.65;color:var(--muted)}
.tile{position:absolute;width:195px;height:182px}
.quote-name{left:617px;top:1927px;font-family:"Cinzel",serif;font-size:28px;color:var(--orange);font-weight:700;letter-spacing:1px}
.quote-org{left:617px;top:1964px;font-size:22px;color:var(--slate)}
.quote-mark{left:612px;top:2000px;font-family:"Cinzel",serif;font-size:110px;line-height:1;color:var(--line)}
.quote-outline{left:785px;top:2050px;width:240px;height:270px;border:3px solid var(--line)}
.quote-card{left:685px;top:2065px;width:265px;height:180px;background:var(--slate);color:#fff;font-size:12px;line-height:1.7;padding:26px 22px}

/* not computer guys */
.band{left:0;top:2401px;width:1200px;height:275px;background:var(--mist)}
.dark-box{left:172px;top:2401px;width:360px;height:330px;background:var(--slate)}
.dark-img{left:207px;top:2436px;width:290px;height:250px;background:linear-gradient(160deg,#3c4348,#9ea3a6 55%,#e6e6e6)}
.not-title{left:617px;top:2460px;font-family:"Cinzel",serif;color:var(--orange);font-size:30px;line-height:1.15}
.not-text{left:617px;top:2548px;width:360px;font-size:12px;line-height:1.6;color:var(--muted)}

/* steps */
.steps-title{left:0;top:2780px;width:1200px;text-align:center;font-family:"Cinzel",serif;font-size:27px;font-weight:700;color:var(--slate);line-height:1.35}
.step{position:absolute;top:2984px;width:190px;height:224px;background:#fff;border:2px solid var(--slate);box-shadow:5px 5px 0 rgba(39,52,58,.25);text-align:center;padding-top:18px}
.step svg{width:46px;height:46px}
.step h4{font-family:"Cinzel",serif;font-size:16px;color:var(--slate);letter-spacing:1px;margin:10px 0 8px}
.step p{font-size:11px;line-height:1.55;color:var(--muted);padding:0 16px}

/* contact */
.contact{left:0;top:3327px;width:1200px;height:635px;background:var(--slate)}
.contact-photo{left:700px;top:3327px;width:500px;height:560px;background:linear-gradient(135deg,#d08b60,#c7784c 50%,#a9603a)}
.form-frame{left:172px;top:3500px;width:480px;height:480px;border:3px solid #fff}
.form-title{left:210px;top:3525px;font-family:"Cinzel",serif;color:#fff;font-size:30px;letter-spacing:1px}
.field{position:absolute;left:220px;width:300px;border-bottom:1px solid rgba(255,255,255,.25);color:rgba(255,255,255,.6);font-size:11px;padding-bottom:8px}
.info-label{position:absolute;left:730px;color:#fff;font-size:13px;font-weight:700;letter-spacing:1px}
.info-text{position:absolute;left:730px;color:#fff;font-size:12px;line-height:1.55;width:300px}
.social{left:730px;top:3892px;display:flex;gap:18px}
.social span{width:12px;height:12px;border-radius:50%;background:rgba(255,255,255,.45);display:block}
.footer-note{left:690px;top:3987px;font-size:11px;color:var(--muted)}
</style>
</head>
<body>

<header class="abs site-header">
  <div class="abs brand">
    <span class="brand-dot"></span>
    <div><div class="brand-name">Brightvale</div><div class="brand-tag">Technology Advisors That Get Business</div></div>
  </div>
  <nav class="abs nav"><span>HOME</span><span>SCHEDULE APPOINTMENT</span></nav>
</header>

<section class="abs hero" role="img" aria-label="Businessman seated by a window looking outside"></section>
<h1 class="abs hero-title">Technology Advisors<br>That "Get" Business</h1>
<p class="abs hero-sub">We help you leverage technology to create a competitive advantage.</p>
<a class="btn" style="left:172px;top:415px;width:195px">Schedule Appointment</a>

<h2 class="abs intro-title">Helping Brands to<br><span>Achieve Success _</span></h2>
<p class="abs intro-text">Enterprise brightvale is a consulting company that works directly with the business owners and leaders of small businesses between 50-200 employees. We help companies make sure they have the right technology to meet their strategic goals. We are the anti-"Computer Guy" and we focus on business outcomes NOT cool technology gadgets.</p>
<a class="btn" style="left:172px;top:905px;width:195px">Schedule Appointment</a>

<div class="abs we-get">
  <h3>We Get...</h3>
  <div class="rule"></div><div class="divide"></div>
  <div class="get-item" style="left:20px;top:110px">REDUCING TIME TO<br>DECISION</div>
  <div class="get-item" style="left:222px;top:110px">ELIMINATING<br>BOTTLENECKS</div>
  <div class="get-item" style="left:20px;top:190px">SCALING UP</div>
  <div class="get-item" style="left:222px;top:190px">LEVERAGE</div>
  <div class="get-item" style="left:20px;top:255px">STRENGTHENING<br>CUSTOMER<br>EXPERIENCE</div>
  <div class="get-item" style="left:222px;top:262px">PREPARING<br>FOR<br>DISRUPTION</div>
</div>

<div class="abs tired-left"></div>
<div class="abs tired-right"></div>
<div class="abs tired-frame"></div>
<h2 class="abs tired-title">Are you tired<br>of "Computer<br>Guys" that...</h2>
<div class="abs timeline"></div>
<div class="tl-item" style="top:1168px"><p>Don't want to be involved in business strategy.</p></div>
<div class="tl-item" style="top:1255px"><p>Say "No!" but do not give options on how to achieve your business outcome.</p></div>
<div class="tl-item" style="top:1350px"><p>Can't explain how a technology will create business value, but insist it is necessary.</p></div>
<div class="tl-item" style="top:1445px"><p>Give you the excuse, "You never asked."</p></div>
<div class="tl-item" style="top:1530px"><p>Recommend technology when a simple process<br>or policy change would have the same</p></div>
<div class="tl-item" style="top:1625px"><p>Suggest expensive solutions that are just thrown away, soon after they are deployed.</p></div>

<p class="abs proof-intro">We get the frustration of working with consultants and experts who don't have or take the time to understand your company goals and vision. We believe technology should serve your business, not the other way around.</p>
<div class="tile" style="left:172px;top:1930px;background:linear-gradient(150deg,#a58a6f,#6f5a48)" role="img" aria-label="Portrait photo of a client"></div>
<div class="tile" style="left:392px;top:1930px;background:linear-gradient(150deg,#7b6a4e,#3f3a2f)" role="img" aria-label="Portrait photo of a client"></div>
<div class="tile" style="left:172px;top:2135px;background:var(--mist)"><svg width="195" height="182" aria-hidden="true"><rect x="25" y="66" width="145" height="50" fill="#e7c532"/></svg></div>
<div class="tile" style="left:392px;top:2135px;background:linear-gradient(150deg,#e8e8e8,#8b8f93)" role="img" aria-label="Portrait photo of a client"></div>

<div class="abs quote-name">Dale Whitmore</div>
<div class="abs quote-org">Harbor Point Fellowship</div>
<div class="abs quote-mark">"</div>
<div class="abs quote-outline"></div>
<div class="abs quote-card">Marcus and the team at Brightvale are in all our strategy meetings whether or not we think technology will be discussed. And, they have brought great insight to better focus even our goals.</div>

<div class="abs band"></div>
<div class="abs dark-box"></div>
<div class="abs dark-img" role="img" aria-label="Businessman facing a chalkboard covered in sketched ideas"></div>
<h2 class="abs not-title">We Are Not<br>"Computer Guys"</h2>
<p class="abs not-text">Computer guys focused on business leaders because they don't have a business mindset. Enterprise brightvale advises on strategy that helps companies apply technology to gain a competitive advantage.</p>
<a class="btn" style="left:617px;top:2630px;width:195px">Schedule Appointment</a>

<h2 class="abs steps-title">The Four Steps to Aligning Technology<br>to your Business Strategy!</h2>
<div class="step" style="left:172px">
  <svg viewBox="0 0 46 46" fill="none" stroke="#c7784c" stroke-width="2"><circle cx="13" cy="30" r="8"/><circle cx="33" cy="30" r="8"/><path d="M19 24h8M9 22l4-12h5v14M37 22l-4-12h-5v14"/></svg>
  <h4>DISCOVER</h4><p>Identify what is going on behind the scenes and create a snapshot of the current infrastructure.</p>
</div>
<div class="step" style="left:396px">
  <svg viewBox="0 0 46 46" fill="none" stroke="#c7784c" stroke-width="2"><rect x="10" y="8" width="26" height="32" rx="2"/><rect x="17" y="5" width="12" height="6"/><path d="M15 20l3 3 5-5M26 21h6M15 31l3 3 5-5M26 32h6"/></svg>
  <h4>PRIORITIZE</h4><p>Invest in the few smart solutions and policies that have the greatest impact on reaching the company goals.</p>
</div>
<div class="step" style="left:620px">
  <svg viewBox="0 0 46 46" fill="none" stroke="#c7784c" stroke-width="2"><circle cx="23" cy="23" r="14"/><circle cx="23" cy="23" r="6"/><path d="M23 3v6M23 37v6M3 23h6M37 23h6"/></svg>
  <h4>IMPLEMENT</h4><p>Implement these things that will give the greatest return on investment.</p>
</div>
<div class="step" style="left:844px">
  <svg viewBox="0 0 46 46" fill="none" stroke="#c7784c" stroke-width="2"><path d="M10 36l18-18M30 8a7 7 0 0 0 8 10l-4-1-3-3zM36 36L16 16M8 8l6 2 2 6-4 0z"/></svg>
  <h4>MAINTAIN</h4><p>Create a system that keeps your technology aligned so strategy adjusts over time.</p>
</div>

<section class="abs contact"></section>
<div class="abs contact-photo" role="img" aria-label="Desk with telephone and notepad under a warm orange tint"></div>
<div class="abs form-frame"></div>
<h2 class="abs form-title">Send message _</h2>
<div class="field" style="top:3612px">Your name</div>
<div class="field" style="top:3660px">Email</div>
<div class="field" style="top:3708px">Subject</div>
<div class="field" style="top:3756px">Phone</div>
<div class="field" style="top:3804px">Address</div>
<div class="field" style="top:3852px;height:88px">Message</div>

<div class="info-label" style="top:3515px">LOCATION</div>
<div class="info-text" style="top:3545px">1420 Ridgeline Parkway, Suite 210,<br>Alder Springs, TX 75500</div>
<div class="info-label" style="top:3600px">EMAIL</div>
<div class="info-text" style="top:3626px">contact@enterprisebrightvale.example</div>
<div class="info-label" style="top:3680px">PHONE</div>
<div class="info-text" style="top:3706px">(555) 014-2290</div>
<div class="abs social"><span></span><span></span><span></span><span></span></div>

<a class="btn" style="left:172px;top:3980px;width:190px">Send Message</a>
<p class="abs footer-note">© Copyright Enterprise Brightvale</p>

</body>
</html>
```